Ostervik Renovations needs a website.

I need a platform for clients to go and learn about what my company does, see pictures of projects, and contact me about their projects. I am a residential remodeler specializing in general contracting services for kitchens, bathrooms, basements, additions, custom interiors, and more. I have attached my logo to be incorporated.

```html
<!DOCTYPE html>
<html lang="en">
<head>
<meta charset="utf-8">
<title>Ostervik Renovations</title>
<link href="https://fonts.googleapis.com/css2?family=Plus+Jakarta+Sans:ital,wght@0,400;0,500;0,600;1,400;1,500&display=swap" rel="stylesheet">
<style>
:root{
  --green:#2f6b26;
  --green-dark:#1c4515;
  --green-text:#275a1d;
  --ink:#1b1b1b;
  --muted:#3a3a3a;
  --light-bg:#efefef;
  --cream:#f6ecd6;
  --cream-border:#d9cdb3;
  --dark:#0b0b0b;
  --tan:#e9d3a6;
  --white:#ffffff;
}
*{box-sizing:border-box;margin:0;padding:0}
html,body{width:1200px;height:4289px;overflow:hidden}
body{position:relative;font-family:"Plus Jakarta Sans",Arial,sans-serif;color:var(--ink);background:var(--white)}
.abs{position:absolute}
.btn{position:absolute;display:flex;align-items:center;justify-content:center;gap:14px;background:var(--green);color:var(--white);font-size:15px;font-weight:500;border:1px solid #4e8a43;box-shadow:4px 4px 0 var(--green-dark),-3px -3px 0 #6c9b62}
.btn svg{width:20px;height:14px}
.eyebrow{position:absolute;font-size:17px;font-weight:600;text-transform:uppercase;letter-spacing:-0.2px}
.photo{position:absolute}

/* hero */
.hero{position:absolute;left:0;top:0;width:1200px;height:712px;background:linear-gradient(135deg,#2a2a2e 0%,#17171a 45%,#0d0d10 100%)}
.brand{position:absolute;display:flex;align-items:center;gap:12px;color:var(--white);font-weight:600;font-size:19px;line-height:1;text-transform:uppercase}
.brand .mark{width:60px;height:60px;border:3px solid var(--white);border-radius:50%}
.nav a{position:absolute;top:66px;color:var(--white);font-size:15px;text-decoration:none}
.hero h1{position:absolute;left:110px;top:228px;color:var(--white);font-size:56px;font-weight:500;line-height:62px;letter-spacing:-1px}
.hero h1 em{font-weight:400}
.hero .sub{position:absolute;left:110px;top:381px;color:var(--white);font-size:21px}
.circle-btn{position:absolute;top:456px;width:40px;height:40px;border:2px solid #c9a640;border-radius:50%;display:flex;align-items:center;justify-content:center}
.tab{position:absolute;top:542px;width:236px;height:170px;background:var(--white);padding:20px}
.tab .num{font-size:54px;font-weight:600;line-height:1}
.tab .lbl{font-size:27px;font-weight:500;margin-top:14px;white-space:nowrap}
.tab.active{background:linear-gradient(160deg,#3a3a3c,#1a1a1c);color:var(--white)}

/* about */
.about{position:absolute;left:0;top:712px;width:1200px;height:658px;background:var(--light-bg)}
.about p{font-size:15px;line-height:34px;color:var(--muted)}

/* cards */
.card{position:absolute;top:1708px;width:310px;height:605px;background:var(--cream);border:1px solid var(--cream-border);border-radius:4px;text-align:center}
.card .photo{left:0;top:0;width:308px;height:342px;border-radius:4px 4px 0 0}
.card h3{position:absolute;left:0;right:0;top:378px;font-size:28px;font-weight:500;color:var(--green-text)}
.card p{position:absolute;left:20px;right:20px;top:428px;font-size:21px;line-height:38px;color:var(--muted)}
.card .btn{left:60px;top:582px;width:185px;height:46px}

.corner{position:absolute;right:0;top:0;width:53px;height:53px;background:#111;display:flex;align-items:center;justify-content:center}

/* contact */
.contact{position:absolute;left:0;top:3303px;width:1200px;height:986px;background:var(--dark);color:var(--white)}
.form-box{position:absolute;left:110px;top:85px;width:532px;height:501px;border:1px solid #5a5a5a}
.field{position:absolute;font-size:15px;color:#d8d8d8;border-bottom:1px solid #6a6a6a;height:40px}
.foot a{position:absolute;top:763px;color:var(--white);font-size:17px;text-decoration:none}
.social{position:absolute;top:830px;width:34px;height:34px;border-radius:50%;background:var(--green)}
</style>
</head>
<body>

<section class="hero">
  <div class="photo" role="img" aria-label="Dark modern kitchen interior with black cabinetry and pendant lights" style="left:0;top:0;width:1200px;height:712px;background:linear-gradient(120deg,rgba(40,40,44,.6),rgba(8,8,10,.9))"></div>
  <div class="brand" style="left:110px;top:40px"><span class="mark"></span><span>Ostervik<br>Renovations</span></div>
  <nav class="nav">
    <a style="left:406px">Home</a><a style="left:489px">About</a><a style="left:574px">Services</a><a style="left:674px">Projects</a><a style="left:774px">Contact</a>
  </nav>
  <svg class="abs" style="left:873px;top:64px" width="22" height="22" viewBox="0 0 22 22" fill="none" stroke="#fff" stroke-width="2"><circle cx="9" cy="9" r="7"/><path d="M14 14l6 6"/></svg>
  <a class="btn" style="left:932px;top:55px;width:158px;height:50px">Get in Touch</a>
  <div class="eyebrow" style="left:110px;top:188px;color:#fff">Residential Remodelling</div>
  <h1>Transforming <em>Homes,</em><br>Elevating <em>Lifestyles.</em></h1>
  <p class="sub">Expert craftsmanship for kitchens, bathrooms, basements, and more.</p>
  <a class="btn" style="left:111px;top:451px;width:185px;height:51px">View Services <svg viewBox="0 0 20 14" fill="none" stroke="#fff" stroke-width="2"><path d="M1 7h17M12 1l6 6-6 6"/></svg></a>
  <div class="circle-btn" style="left:381px"><svg width="14" height="14" viewBox="0 0 14 14" fill="none" stroke="#fff" stroke-width="2"><path d="M9 2L4 7l5 5"/></svg></div>
  <div class="circle-btn" style="left:429px"><svg width="14" height="14" viewBox="0 0 14 14" fill="none" stroke="#fff" stroke-width="2"><path d="M5 2l5 5-5 5"/></svg></div>
  <div class="tab" style="left:381px"><div class="num">01</div><div class="lbl">Custom Interior</div></div>
  <div class="tab active" style="left:616px"><div class="num">02</div><div class="lbl">Modular Kitchen</div></div>
  <div class="tab" style="left:852px"><div class="num">03</div><div class="lbl">Basements</div></div>
  <div class="tab" style="left:1088px;width:112px;overflow:hidden"><div class="num">04</div><div class="lbl">Living Room</div></div>
</section>

<section class="about">
  <div class="abs" style="left:110px;top:80px;font-size:52px;line-height:1">12+ <span style="font-size:27px">Years of Experience</span></div>
  <div class="photo" role="img" aria-label="Architectural sketch of a glass garden pavilion" style="left:75px;top:162px;width:458px;height:274px;background:radial-gradient(ellipse at center,#dcdcdc,#efefef 70%)"></div>
  <div class="abs" style="left:110px;top:458px;font-size:28px;font-style:italic">“Creating Timeless Masterpieces”</div>
  <a class="btn" style="left:111px;top:521px;width:197px;height:49px">Learn More on Us <svg viewBox="0 0 20 14" fill="none" stroke="#fff" stroke-width="2"><path d="M1 7h17M12 1l6 6-6 6"/></svg></a>
  <svg class="abs" style="left:354px;top:523px" width="40" height="40" viewBox="0 0 40 40" fill="none" stroke="#2f6b26" stroke-width="2"><circle cx="20" cy="20" r="18"/><path d="M13 12c0 9 6 15 15 15l2-4-4-2-2 2c-3-1-6-4-7-7l2-2-2-4z"/></svg>
  <div class="abs" style="left:409px;top:520px;font-size:15px;color:var(--green-text);font-weight:500">Call Us</div>
  <div class="abs" style="left:409px;top:546px;font-size:12px">555 - 0148 2290</div>

  <div class="eyebrow" style="left:599px;top:85px;color:var(--green-text)">About Us</div>
  <h2 class="abs" style="left:599px;top:122px;font-size:40px;font-weight:500">Who We Are</h2>
  <div class="abs" style="left:599px;top:186px;width:520px">
    <p>Ostervik Renovations is a trusted name in residential remodeling, specializing in high-quality renovations for kitchens, bathrooms, basements, and home additions.</p>
    <p>Our goal is to transform your house into the home of your dreams.</p>
  </div>
  <div class="photo" role="img" aria-label="Bright white kitchen with dining table and pendant lights" style="left:599px;top:360px;width:489px;height:211px;background:linear-gradient(135deg,#d9d6cf,#8c8a86 60%,#4a4a4a)"></div>
</section>

<section class="services">
  <div class="eyebrow" style="left:110px;top:1452px;color:var(--green-text)">Services We Offer</div>
  <h2 class="abs" style="left:110px;top:1497px;font-size:43px;font-weight:500;line-height:55px">From concept to<br>completion, we<br>bring your vision to life.</h2>
  <p class="abs" style="left:533px;top:1504px;font-size:15px;line-height:30px;width:360px">Expert craftsmanship for kitchens, bathrooms, basements, and more.</p>
  <a class="btn" style="left:911px;top:1513px;width:177px;height:50px">View All Services</a>

  <article class="card" style="left:111px">
    <div class="photo" role="img" aria-label="Wooden staircase with built-in drawers" style="background:linear-gradient(135deg,#e6e0d8,#b78a5c 60%,#8a5f38)"></div>
    <h3>Modular Kitchen</h3>
    <p>Modern, functional, and stylish kitchen renovations and interior and designs.</p>
    <a class="btn">View Details <svg viewBox="0 0 20 14" fill="none" stroke="#fff" stroke-width="2"><path d="M1 7h17M12 1l6 6-6 6"/></svg></a>
  </article>
  <article class="card" style="left:446px">
    <div class="photo" role="img" aria-label="Luxury bathroom with arched mirror and stone wall" style="background:linear-gradient(135deg,#7c7468,#c9b79a 50%,#5d5a55)"></div>
    <h3>Luxury Bathrooms</h3>
    <p>Luxury and comfort with high-end bathroom upgrades.</p>
    <a class="btn">View Details <svg viewBox="0 0 20 14" fill="none" stroke="#fff" stroke-width="2"><path d="M1 7h17M12 1l6 6-6 6"/></svg></a>
  </article>
  <article class="card" style="left:780px">
    <div class="photo" role="img" aria-label="Living room with beige sofa and open kitchen" style="background:linear-gradient(135deg,#dcdcd6,#a89a86 60%,#6e5e4e)"></div>
    <h3>Custom Interiors</h3>
    <p>Tailored interior solutions to match your lifestyle and beautify your spaces.</p>
    <a class="btn">View Details <svg viewBox="0 0 20 14" fill="none" stroke="#fff" stroke-width="2"><path d="M1 7h17M12 1l6 6-6 6"/></svg></a>
  </article>
</section>

<section class="projects">
  <div class="eyebrow" style="left:110px;top:2509px;color:var(--green-text)">Our Projects</div>
  <h2 class="abs" style="left:110px;top:2555px;font-size:43px;font-weight:500;line-height:55px">Explore our recent<br>projects and see<br>the transformation.</h2>
  <div class="abs" style="left:110px;top:2740px;font-size:27px;font-style:italic">“ Our Work Speak for Itself ”</div>

  <div class="photo" role="img" aria-label="Dark kitchen island with black bar stools and wine rack" style="left:599px;top:2514px;width:489px;height:279px;background:linear-gradient(135deg,#2a2a2a,#5a5550 55%,#8a6a4a)"><span class="corner"><svg width="16" height="16" viewBox="0 0 16 16" fill="none" stroke="#fff" stroke-width="2"><path d="M3 13L13 3M5 3h8v8"/></svg></span></div>
  <div class="photo" role="img" aria-label="White kitchen with dining table and pendant lights" style="left:110px;top:2816px;width:471px;height:296px;background:linear-gradient(135deg,#d9d6cf,#8c8a86 60%,#4a4a4a)"><span class="corner"><svg width="16" height="16" viewBox="0 0 16 16" fill="none" stroke="#fff" stroke-width="2"><path d="M3 13L13 3M5 3h8v8"/></svg></span></div>
  <div class="photo" role="img" aria-label="Bathroom with stone feature wall and floating vanity" style="left:599px;top:2816px;width:489px;height:296px;background:linear-gradient(135deg,#7c7468,#c9b79a 50%,#5d5a55)"><span class="corner"><svg width="16" height="16" viewBox="0 0 16 16" fill="none" stroke="#fff" stroke-width="2"><path d="M3 13L13 3M5 3h8v8"/></svg></span></div>

  <a class="btn" style="left:489px;top:3164px;width:227px;height:50px">View All Our Projects <svg viewBox="0 0 20 14" fill="none" stroke="#fff" stroke-width="2"><path d="M1 7h17M12 1l6 6-6 6"/></svg></a>
</section>

<section class="contact">
  <form class="form-box">
    <div class="field" style="left:59px;top:63px;width:175px">First Name</div>
    <div class="field" style="left:290px;top:63px;width:175px">Last Name</div>
    <div class="field" style="left:59px;top:153px;width:175px">Email Address</div>
    <div class="field" style="left:290px;top:153px;width:175px">Phone Number</div>
    <div class="field" style="left:59px;top:250px;width:406px;height:94px">Your Message</div>
    <a class="btn" style="left:156px;top:395px;width:220px;height:50px">Send the Message <svg viewBox="0 0 20 14" fill="none" stroke="#fff" stroke-width="2"><path d="M1 7h17M12 1l6 6-6 6"/></svg></a>
  </form>
  <h2 class="abs" style="left:729px;top:152px;font-size:43px;font-weight:500">Get in Touch</h2>
  <p class="abs" style="left:732px;top:237px;width:340px;font-size:17px;line-height:35px;color:#e6e6e6">Get in touch to discuss your project and requirements get a free quote .</p>
  <p class="abs" style="left:730px;top:350px;font-size:27px;line-height:45px;font-style:italic;color:var(--tan)">“ Let’s Conect Today<br>and Let’s Build<br>Something Amazing ”.</p>

  <div class="abs" style="left:110px;top:673px;width:978px;height:1px;background:#444"></div>
  <div class="brand" style="left:112px;top:723px"><span class="mark" style="width:68px;height:68px"></span><span>Ostervik<br>Renovations</span></div>
  <nav class="foot">
    <a style="left:589px">Home</a><a style="left:687px">About</a><a style="left:786px">Services</a><a style="left:904px">Projects</a><a style="left:1020px">Contact</a>
  </nav>
  <p class="abs" style="left:110px;top:832px;width:380px;font-size:17px;line-height:34px">We are Committed to quality craftsmanship and client satisfaction.</p>
  <div class="abs" style="left:676px;top:837px;font-size:17px">Follow Our Socials</div>
  <span class="social" style="left:867px"></span><span class="social" style="left:930px"></span><span class="social" style="left:993px"></span><span class="social" style="left:1055px"></span>
  <div class="abs" style="left:112px;top:921px;font-size:12px;color:#ddd">Copyright ©2025 OstervikRenovations. All rights reserved.</div>
  <div class="abs" style="left:894px;top:921px;font-size:12px">Privacy</div>
  <div class="abs" style="left:962px;top:921px;font-size:12px">Support</div>
  <div class="abs" style="left:1037px;top:921px;font-size:12px">Licences</div>
</section>

</body>
</html>
```